Carte d'affaire bilingue

Nous avons besoin d'une carte d'affaire pour notre entreprise spécialisée en vente et achat de terrain. Nous sommes une agence immobilière et nous voulons une carte avec le recto en Français et le verso en anglais. Nous voulons une image sobre et épurée. Nous avons de la clientèle internationale et nous voulons une carte très professionnelle mais qui se démarque. Nous voulons cibler une clientèle commerciale, industrielle, contracteurs et promoteurs immobiliers.
Updates

Hi everybody, we saw all your conception and we are approching of what we like but the "WOW" is missing.

We love the little sign to specify (phone or email) but we can put them in a square to make like our logo, we love also dark gray not lite gray, we also love the stainless lines. In our logo you can see a little sign +. For us is signyfy " Always further" so if you can put many little +++++ in the conception somewhere very discret it will be appreciate. We also like a kind of round that make a magnyfying glass, because we search land we found opportunity.

Thank you

Reason: I ask different things in the last day but no one do what i am asking for. For the conception # 3016702 that we love we ask changes.

We like simplicity, urban design, corporate, international. The card must have one side in french and the other side in english. We like dark gray,silver, and a little bit of green.

Target Market(s)

Investors, developers, construction builders, etc...

Font styles to use
Serif
Sans Serif

Requirements
Must have
• logo
La mention: Agence immobilière (Francais) / Real Estate Agency (anglais)
Sous le nom: Courtier immobilier agréé (Français) / Real Estate Broker

```html
<!DOCTYPE html>
<html lang="fr">
<head>
<meta charset="utf-8">
<title>Ground Scout – Cartes d'affaires</title>
<link rel="stylesheet" href="https://fonts.googleapis.com/css2?family=Didact+Gothic&family=Open+Sans:wght@400;700&display=swap">
<style>
  :root {
    --backdrop: #e6e6e4;
    --card: #ffffff;
    --green: #1f7a3a;
    --dark-gray: #4a4a4a;
    --ink: #2b2b2b;
    --silver: #b8bcbf;
  }
  * { margin: 0; padding: 0; box-sizing: border-box; }
  html, body { width: 1200px; height: 960px; overflow: hidden; }
  body {
    background: var(--backdrop);
    font-family: "Didact Gothic", "Open Sans", sans-serif;
    color: var(--ink);
    position: relative;
  }
  .card {
    position: absolute;
    left: 250px;
    width: 700px;
    height: 400px;
    background: var(--card);
    box-shadow: 0 6px 22px rgba(0,0,0,.14);
  }
  .card--front { top: 60px; }
  .card--back { top: 500px; }

  .brand { position: absolute; left: 48px; top: 42px; }
  .brand__row { display: flex; align-items: center; gap: 16px; }
  .brand__square { width: 58px; height: 58px; background: var(--green); }
  .brand__name {
    font-size: 40px; line-height: 1; color: var(--dark-gray);
    letter-spacing: 1px; text-transform: uppercase;
  }
  .brand__agency {
    margin-top: 10px; margin-left: 74px;
    padding-top: 6px;
    border-top: 2px solid var(--silver);
    font-size: 19px; color: var(--ink);
    width: 330px; text-align: right;
  }

  .person { position: absolute; left: 60px; top: 180px; }
  .person__name { font-size: 34px; color: var(--green); }
  .person__title { font-size: 21px; color: var(--dark-gray); line-height: 1.25; margin-top: 4px; }

  .address {
    position: absolute; left: 60px; bottom: 44px;
    font-size: 19px; line-height: 1.35; color: var(--ink);
  }

  .contact {
    position: absolute; right: 48px; bottom: 40px;
    text-align: right; font-size: 19px; line-height: 1.35; color: var(--ink);
  }
  .contact__label { color: var(--green); font-family: "Open Sans", sans-serif; font-weight: 700; font-size: 17px; }
</style>
</head>
<body>

  <section class="card card--front" lang="fr">
    <div class="brand">
      <div class="brand__row">
        <span class="brand__square"></span>
        <span class="brand__name">L'Éclaireur Foncier</span>
      </div>
      <div class="brand__agency">Agence immobilière</div>
    </div>
    <div class="person">
      <p class="person__name">Sophie Marchand</p>
      <p class="person__title">Courtier Immobilier Agréé, D.A.<br>Vice Présidente</p>
    </div>
    <p class="address">218 B, blv. Industriel, 3e<br>Laval, Qc, H7L 4R2</p>
    <div class="contact">
      <p>www.groundscout.ca</p>
      <p>s.marchand@groundscout.ca</p>
      <p><span class="contact__label">Téléphone</span> 514.555.0147</p>
      <p><span class="contact__label">Télécopie</span> 450.555.0192</p>
      <p><span class="contact__label">Sans Frais</span> 1.866.555.0110</p>
    </div>
  </section>

  <section class="card card--back" lang="en">
    <div class="brand">
      <div class="brand__row">
        <span class="brand__square"></span>
        <span class="brand__name">Ground Scout</span>
      </div>
      <div class="brand__agency">Real Estate Agency</div>
    </div>
    <div class="person">
      <p class="person__name">Sophie Marchand</p>
      <p class="person__title">Real Estate Broker, D.A.<br>Vice President</p>
    </div>
    <p class="address">218 B, blv. Industriel, 3e<br>Laval, Qc, H7L 4R2</p>
    <div class="contact">
      <p>www.groundscout.ca</p>
      <p>s.marchand@groundscout.ca</p>
      <p><span class="contact__label">Phone</span> 514.555.0147</p>
      <p><span class="contact__label">Fax</span> 450.555.0192</p>
      <p><span class="contact__label">Toll Free</span> 1.866.555.0110</p>
    </div>
  </section>

</body>
</html>
```